Dorian's Lawn Service needs a postcard design

I need a design to attract lawn cutting customers. I am a high school junior, focusing on my city and the neighboring city. I think it would be advantageous to let my potential clients know I am earning money for my college education. They should also know, I will be working side by side with my father, who operated his own lawn service for 20 years, so they can be assured of a quality result for their lawn. I will be using state of the art, commercial equipment.

A few things that are unique to my service are; my mower weighs half of what other commercial mowers do (a softer footprint), my mower does NOT throw clippings into mulch or flower beds, at an additional charge I offer bagging of the clippings and/or dog waste clean-up. I am thinking about a two-sided design. I would also like a cartoon style picture of myself riding my mower. If this is something you can create, I can send you a photo of myself and a photo of my mower. If not, I can get this drawing done separately, then send it to you, I would just need to know what kind of file you would need it in. I am not going to have a business name, I want to introduce myself as Dorian to keep it simple and personal. We can add a coupon to the postcard, offering one free cut with commitment to a full 26 week season. The name of my high school is Marlowe High.

The cartoon picture attached is our logo.

Target Market(s)

Homeowners that use a commercial lawn cutting service, homeowners that need a temporary service while they are on vacation

Industry/Entity Type

School

Colors
3176b5
9bcb3c

Requirements
Must have
• An appeal for people to want to help me earn money for my college education. A clear idea they will be getting top notch service. I definitely want a drawing of myself on my mower. Phone # 612-905-3817
• design must work with parcelvaro.com/routeflyermailing guidelines

```html
<!DOCTYPE html>
<html lang="en">
<head>
<meta charset="utf-8">
<title>Dorian's Lawn Service – Postcard</title>
<link rel="stylesheet" href="https://fonts.googleapis.com/css2?family=Arimo:wght@700&family=Oswald:wght@400;500&family=Josefin+Sans:wght@400;600&display=swap">
<style>
  :root {
    --bg: #2a2a2a;
    --brand-blue: #1f62a8;
    --accent-blue: #2b3f9e;
    --grass-light: #7fbf45;
    --grass-mid: #4f9a2c;
    --grass-dark: #2f6e1e;
    --panel-green: #7ab940;
    --band-green: #3f9a3a;
    --tab-green: #2e6e35;
    --curve-dark: #2f6b2a;
    --white: #ffffff;
    --ink: #111111;
  }
  * { box-sizing: border-box; margin: 0; padding: 0; }
  html, body { width: 960px; height: 1200px; overflow: hidden; }
  body { background: var(--bg); position: relative; font-family: "Josefin Sans", sans-serif; }

  .card { position: absolute; left: 128px; width: 704px; overflow: hidden; }

  /* Front */
  .card-front { top: 38px; height: 546px; }
  .front-art {
    position: absolute; inset: 0;
    background: linear-gradient(160deg, var(--grass-light) 0%, var(--grass-mid) 55%, var(--grass-dark) 100%);
  }
  .front-title {
    position: absolute; left: 327px; top: 56px;
    font-family: "Arimo", sans-serif; font-weight: 700; font-size: 41px; line-height: 53px;
    color: var(--brand-blue); letter-spacing: 0.5px;
    -webkit-text-stroke: 1.5px var(--white); paint-order: stroke fill;
    text-shadow: 0 0 2px var(--white), 1px 1px 0 var(--white), -1px -1px 0 var(--white);
  }
  .band {
    position: absolute; right: 0;
    background: linear-gradient(90deg, rgba(63,154,58,0) 0%, var(--band-green) 25%, var(--band-green) 100%);
    font-family: "Oswald", sans-serif; font-weight: 500; text-transform: uppercase;
  }
  .band-appeal { top: 260px; width: 352px; height: 80px; padding: 12px 40px 0 0; text-align: right;
    font-size: 25px; line-height: 33px; color: var(--ink); }
  .band-offer { top: 475px; width: 350px; height: 48px; padding: 4px 38px 0 0; text-align: right;
    font-size: 29px; line-height: 38px; color: var(--white); }

  /* Back */
  .card-back { top: 625px; height: 544px; background: var(--white); }
  .back-shape { position: absolute; inset: 0; }
  .tab {
    position: absolute; left: 0; top: 23px; width: 269px; height: 50px;
    background: var(--tab-green); border-right: 6px solid #b9d98f;
    font-family: "Oswald", sans-serif; font-size: 31px; line-height: 48px; color: var(--white); padding-left: 44px;
  }
  .avatar {
    position: absolute; left: 304px; top: 15px; width: 106px; height: 106px; border-radius: 50%;
    background: radial-gradient(circle at 50% 40%, #3f7dc4, #1c4f98);
  }
  .features { position: absolute; left: 20px; top: 100px; list-style: none; }
  .features li { position: relative; padding-left: 24px; font-size: 16.5px; line-height: 22px; color: var(--ink); margin-bottom: 7px; }
  .features li b { font-weight: 600; color: var(--white); }
  .features svg { position: absolute; left: 0; top: 3px; width: 14px; height: 14px; }
  .extras-title { font-family: "Arimo", sans-serif; font-size: 22px; color: var(--accent-blue); margin: 3px 0 6px 24px; }
  .coupon { position: absolute; left: 45px; top: 346px; font-size: 19.5px; line-height: 25px; color: var(--white); }
  .cta { position: absolute; left: 37px; top: 405px; font-family: "Oswald", sans-serif; font-size: 21px; color: var(--ink); }
  .phone { position: absolute; left: 37px; top: 437px; display: flex; align-items: center; gap: 12px;
    font-family: "Arimo", sans-serif; font-weight: 400; font-size: 30px; color: var(--accent-blue); }
  .phone svg { width: 28px; height: 28px; }
  .stamp { position: absolute; left: 578px; top: 32px; width: 93px; height: 106px; border: 1px solid #333; }
  .address-line { position: absolute; left: 448px; width: 222px; height: 1px; background: #333; }
</style>
</head>
<body>

<section class="card card-front">
  <div class="front-art" role="img" aria-label="Cartoon of Dorian riding a red zero-turn mower on a striped green lawn"></div>
  <h1 class="front-title">DORIAN'S<br>LAWN CUTTING<br>SERVICE</h1>
  <p class="band band-appeal">Help me earn money for<br>my college education</p>
  <p class="band band-offer">Ask me about a free cut</p>
</section>

<section class="card card-back">
  <svg class="back-shape" viewBox="0 0 704 544" width="704" height="544" aria-hidden="true">
    <path d="M0 0 H330 C420 120 420 340 368 544 H0 Z" fill="var(--curve-dark)"/>
    <path d="M0 0 H312 C398 120 398 340 350 544 H0 Z" fill="var(--panel-green)"/>
    <rect x="184" y="480" width="200" height="64" fill="var(--white)"/>
  </svg>

  <div class="tab">Dorian's Service</div>
  <div class="avatar" role="img" aria-label="Small cartoon of Dorian on his mower"></div>

  <ul class="features">
    <li><svg viewBox="0 0 14 14"><circle cx="7" cy="7" r="6" fill="none" stroke="#1f4f9a" stroke-width="1.3"/><path d="M4 7.2l2 2 4-4.2" fill="none" stroke="#1f4f9a" stroke-width="1.4"/></svg><b>Quality-</b> Working with my Dad,<br>who owned a lawn service for 20 years</li>
    <li><svg viewBox="0 0 14 14"><circle cx="7" cy="7" r="6" fill="none" stroke="#1f4f9a" stroke-width="1.3"/><path d="M4 7.2l2 2 4-4.2" fill="none" stroke="#1f4f9a" stroke-width="1.4"/></svg><b>Care-</b> I will treat your yard like my own</li>
    <li><svg viewBox="0 0 14 14"><circle cx="7" cy="7" r="6" fill="none" stroke="#1f4f9a" stroke-width="1.3"/><path d="M4 7.2l2 2 4-4.2" fill="none" stroke="#1f4f9a" stroke-width="1.4"/></svg><b>Mower-</b> Half the weight of other mowers<br>&amp; doesn't blow clippings into mulch</li>
    <li class="extras-title" style="padding-left:0">EXTRAS</li>
    <li><svg viewBox="0 0 14 14"><circle cx="7" cy="7" r="6" fill="none" stroke="#1f4f9a" stroke-width="1.3"/><path d="M4 7.2l2 2 4-4.2" fill="none" stroke="#1f4f9a" stroke-width="1.4"/></svg><b>Bagging-</b> I can bag the clippings</li>
    <li><svg viewBox="0 0 14 14"><circle cx="7" cy="7" r="6" fill="none" stroke="#1f4f9a" stroke-width="1.3"/><path d="M4 7.2l2 2 4-4.2" fill="none" stroke="#1f4f9a" stroke-width="1.4"/></svg><b>Dog poop-</b> I can scoop it for you</li>
    <li><svg viewBox="0 0 14 14"><circle cx="7" cy="7" r="6" fill="none" stroke="#1f4f9a" stroke-width="1.3"/><path d="M4 7.2l2 2 4-4.2" fill="none" stroke="#1f4f9a" stroke-width="1.4"/></svg><b>One time cut-</b> While you are on vacation</li>
  </ul>

  <p class="coupon">One Free Cut With Commitment<br>To A Full 26 Week Season</p>
  <p class="cta">CALL ME TO SET UP A FREE QUOTE</p>
  <p class="phone">
    <svg viewBox="0 0 28 28" aria-hidden="true"><circle cx="14" cy="14" r="12.5" fill="none" stroke="currentColor" stroke-width="2"/><path d="M10 7.5c-1.5 1-2 2.5-1.3 4.5 1.3 3.6 4 6.4 7.5 7.7 2 .7 3.4.2 4.4-1.3l-2.6-2.3-1.8 1.2c-1.9-.8-3.3-2.3-4.2-4.2l1.2-1.8z" fill="currentColor"/></svg>
    612-905-3817
  </p>

  <div class="stamp"></div>
  <div class="address-line" style="top:304px"></div>
  <div class="address-line" style="top:342px"></div>
  <div class="address-line" style="top:379px"></div>
</section>

</body>
</html>
```